Visual Print Advert for Hair & Makeup Artist

One page colour visual advertisement required for a hair and makeup artist business using pictures and logo with brief description and contact details. MUST have plain white background. All information will be provided I just need someone to put it in a good layout.
Professional, clean and appealing to the eye. Don't want it to look over crowded or busy.
Layout should feature 2-7 photos, without making the page look too busy. Can use any of the photos provided and you are welcome to crop them to change the orientation of the photo.
Content and typeface should fit in with logo and be modern but appeal to the female target audience of brides in Australia aged 22-40yo.
Advertisement is be be used in a bridal magazine and other print media for business advertising purposes.
Updates

Target Market(s)

Future brides in Australia aged 22 - 40yo - females only

Industry/Entity Type

Business

Colors
e34197
ffffff
eda3c7

Requirements
Must have
• White background
Should not have
• NO script writing as it doesn't fit with the logo.

```html
<!DOCTYPE html>
<html lang="en">
<head>
<meta charset="utf-8">
<title>Lumora Makeup Artistry – Bridal Advert</title>
<link rel="stylesheet" href="https://fonts.googleapis.com/css2?family=Exo+2:wght@400;500&family=Raleway:wght@300;400&display=swap">
<style>
  :root {
    --magenta: #d4177f;
    --magenta-bright: #e34197;
    --magenta-deep: #b3105f;
    --crimson: #a3072f;
    --crimson-dark: #8c0526;
    --blush: #eda3c7;
    --paper: #ffffff;
    --ink: #2b2b2b;
    --frame-shadow: rgba(120, 20, 70, 0.28);
  }
  * { box-sizing: border-box; margin: 0; padding: 0; }
  html, body { width: 890px; height: 1200px; overflow: hidden; background: #f2f2f2; }
  .advert {
    position: relative; width: 890px; height: 1200px;
    background: var(--paper); overflow: hidden;
    font-family: "Exo 2", sans-serif;
  }
  .hero-band {
    position: absolute; left: 0; top: 20px; width: 420px; height: 500px;
    background: linear-gradient(90deg, var(--crimson-dark) 0%, var(--crimson) 55%, var(--magenta) 85%, var(--magenta-bright) 100%);
  }
  .stripe-band {
    position: absolute; left: 420px; top: 290px; width: 470px; height: 75px;
    background: linear-gradient(180deg, #c8125a 0%, #b80c4c 25%, #a8083e 50%, #9a0633 75%, #8c0526 100%);
  }
  .intro-band {
    position: absolute; left: 420px; top: 365px; width: 470px; height: 190px;
    background: linear-gradient(180deg, var(--magenta-deep), var(--magenta));
  }
  .divider-band {
    position: absolute; left: 0; top: 520px; width: 890px; height: 40px;
    background: var(--magenta);
  }
  .polaroid {
    position: absolute; background: var(--paper);
    box-shadow: 2px 4px 10px var(--frame-shadow);
  }
  .polaroid .photo { position: absolute; left: 12px; top: 12px; right: 12px; }
  .polaroid--hero { left: 28px; top: 45px; width: 420px; height: 500px; transform: rotate(2deg); }
  .polaroid--hero .photo { height: 420px;
    background: radial-gradient(ellipse at 55% 40%, #e7c4b4 0%, #c99a88 35%, #3a2a2a 70%, #9a96a4 100%); }
  .polaroid--portrait { left: 650px; top: 150px; width: 205px; height: 220px; transform: rotate(-3deg); }
  .polaroid--portrait .photo { height: 180px;
    background: linear-gradient(135deg, #5a5a5a, #cfcfcf 55%, #8a8a8a); }
  .polaroid--car { left: 40px; top: 590px; width: 210px; height: 230px; transform: rotate(-10deg); }
  .polaroid--car .photo { height: 180px;
    background: linear-gradient(160deg, #e9e9e6 0%, #cfa48a 40%, #b8232b 70%, #d9d9d6 100%); }
  .polaroid--closeup { left: 255px; top: 610px; width: 200px; height: 225px; }
  .polaroid--closeup .photo { height: 190px;
    background: radial-gradient(ellipse at 50% 50%, #e2b8a2 0%, #a57860 45%, #4a3328 100%); }
  .polaroid--hairstyle { left: 445px; top: 580px; width: 215px; height: 230px; transform: rotate(5deg); }
  .polaroid--hairstyle .photo { height: 190px;
    background: linear-gradient(150deg, #dfe3e6 0%, #c58d6a 40%, #e8dcd8 75%, #dfe6ea 100%); }
  .bride-figure {
    position: absolute; left: 660px; top: 555px; width: 230px; height: 605px; z-index: 2;
    background: linear-gradient(180deg, #7b4d3a 0%, #e4c0ab 30%, #f2ece6 55%, #f7f3ef 100%);
  }
  .brand {
    position: absolute; left: 470px; top: 48px; width: 390px; text-align: right;
    color: var(--ink); font-family: "Raleway", sans-serif; font-weight: 300;
  }
  .brand__name { font-size: 58px; letter-spacing: 6px; line-height: 1; }
  .brand__tag { font-size: 14px; letter-spacing: 2.5px; margin-top: 6px; }
  .intro {
    position: absolute; left: 472px; top: 382px; width: 400px;
    text-align: center; color: var(--paper);
    font-size: 26px; line-height: 40px; font-weight: 400;
  }
  .promise {
    position: absolute; left: 70px; top: 858px; width: 560px;
    text-align: center; color: var(--magenta);
    font-size: 25px; line-height: 38px;
  }
  .contact-bar {
    position: absolute; left: 0; top: 1040px; width: 890px; height: 120px;
    background: linear-gradient(180deg, var(--magenta-deep), var(--magenta));
    border-top: 4px solid var(--blush);
  }
  .contact-list {
    position: absolute; left: 40px; top: 10px; list-style: none;
    color: var(--paper); font-family: "Raleway", sans-serif; font-weight: 400;
    font-size: 22px; letter-spacing: 2px;
  }
  .contact-list li { display: flex; align-items: center; height: 34px; }
  .contact-list svg { width: 18px; height: 18px; margin-right: 12px; flex: none; }
</style>
</head>
<body>
<main class="advert">
  <div class="hero-band"></div>
  <div class="stripe-band"></div>
  <div class="intro-band"></div>
  <div class="divider-band"></div>

  <figure class="polaroid polaroid--hero">
    <div class="photo" role="img" aria-label="Close-up portrait of a bride with dark hair and a veil"></div>
  </figure>

  <header class="brand">
    <div class="brand__name">LUMORA</div>
    <div class="brand__tag">MAKEUP ARTISTRY</div>
  </header>

  <figure class="polaroid polaroid--portrait">
    <div class="photo" role="img" aria-label="Black and white portrait of a smiling bride"></div>
  </figure>

  <p class="intro">Professionally trained and<br>certified mobile Hair &amp;<br>Makeup Artists with<br>over 10 years experience</p>

  <figure class="polaroid polaroid--car">
    <div class="photo" role="img" aria-label="Bride smiling from the window of a vintage car"></div>
  </figure>
  <figure class="polaroid polaroid--closeup">
    <div class="photo" role="img" aria-label="Bride looking down showing eye makeup"></div>
  </figure>
  <figure class="polaroid polaroid--hairstyle">
    <div class="photo" role="img" aria-label="Bridal updo decorated with small flowers"></div>
  </figure>

  <p class="promise">We specialise in naturally<br>enhancing your<br>beauty to have you looking and feeling<br>your best on your special day.</p>

  <footer class="contact-bar">
    <ul class="contact-list">
      <li>
        <svg viewBox="0 0 20 20" aria-hidden="true"><circle cx="10" cy="10" r="10" fill="#fff"/><path d="M6.5 5.5l2 -0.5 1 2.5-1.2 1a6 6 0 0 0 3 3l1-1.2 2.5 1-0.5 2c-4 0.5-8.3-3.8-7.8-7.8z" fill="#d4177f"/></svg>
        0400 123 456
      </li>
      <li>
        <svg viewBox="0 0 20 20" aria-hidden="true"><circle cx="10" cy="10" r="10" fill="#fff"/><rect x="5" y="6.5" width="10" height="7" fill="none" stroke="#d4177f" stroke-width="1.4"/><path d="M5 6.5l5 4 5-4" fill="none" stroke="#d4177f" stroke-width="1.4"/></svg>
        mia@lumoramakeup.com.au
      </li>
      <li>
        <svg viewBox="0 0 20 20" aria-hidden="true"><circle cx="10" cy="10" r="10" fill="#fff"/><circle cx="10" cy="10" r="5.5" fill="none" stroke="#d4177f" stroke-width="1.3"/><ellipse cx="10" cy="10" rx="2.4" ry="5.5" fill="none" stroke="#d4177f" stroke-width="1.1"/><path d="M4.5 10h11" stroke="#d4177f" stroke-width="1.1"/></svg>
        www.lumoramakeup.com.au
      </li>
    </ul>
  </footer>

  <div class="bride-figure" role="img" aria-label="Bride in a lace gown with a flower crown holding a bouquet"></div>
</main>
</body>
</html>
```